Clean Stationary Design For Print Shop

I need a clean stationary set that properly represents a local print and copy shop to make it look amazing. It should do the following:
- Compliment the color scheme of the logo.
- Be clean and sharp.
- Be colorful but but balanced.

This is what I need designed:
- Business Card
- Letter Head
- Envelop

Target Market(s)

Local customers and businesses, including hospitals and schools.

Industry/Entity Type

Digital Printing

Requirements
Must have
• Clean business card with logo on front and full color back with faded logo on it and social icons with @tollworthmarks beside each one (Pagelark & Glimmora).

```html
<!DOCTYPE html>
<html lang="en">
<head>
<meta charset="utf-8">
<title>Tollworth Marks — Stationery Set</title>
<link rel="stylesheet" href="https://fonts.googleapis.com/css2?family=Fira+Sans:wght@400;600&family=Open+Sans:wght@700&family=Montserrat:wght@400&display=swap">
<style>
  :root {
    --stage: #bcbdc0;
    --paper: #ffffff;
    --ink: #050608;
    --brand-red: #ee344d;
    --steel: #858688;
    --muted: #6d6e71;
  }
  html, body { margin: 0; padding: 0; overflow: hidden; background: var(--stage); }
  .canvas { display: block; width: 1200px; height: 965px; }
  .sheet { filter: drop-shadow(6px 8px 8px rgba(0,0,0,.28)); }
  .fill-paper { fill: var(--paper); }
  .fill-ink { fill: var(--ink); }
  .fill-red { fill: var(--brand-red); }
  .fill-steel { fill: var(--steel); }
  .brand-name { font-family: "Fira Sans", sans-serif; font-weight: 400; }
  .tagline { font-family: "Open Sans", sans-serif; font-weight: 700; }
  .contact { font-family: "Montserrat", sans-serif; font-weight: 400; fill: var(--paper); }
  .person { font-family: "Fira Sans", sans-serif; font-weight: 400; }
</style>
</head>
<body>
<svg class="canvas" viewBox="0 0 2156 1733" xmlns="http://www.w3.org/2000/svg" role="group" aria-label="Tollworth Marks letterhead, envelope and business cards">
  <rect width="2156" height="1733" fill="var(--stage)"/>

  <!-- Letterhead -->
  <g class="letterhead">
    <rect class="sheet fill-paper" x="257" y="105" width="1076" height="1522"/>
    <polygon class="fill-steel" points="257,105 363,105 257,255"/>
    <polygon class="fill-ink" points="363,105 1333,105 1333,163 970,163 868,292 257,292 257,255"/>
    <polygon class="fill-red" points="980,179 1333,179 1333,221 946,221"/>
    <polygon class="fill-red" points="257,292 810,292 779,338 257,338"/>
    <polygon class="fill-ink" points="257,338 363,338 257,480"/>
    <g class="letterhead-logo">
      <rect class="fill-paper" x="405" y="168" width="52" height="62"/>
      <text class="brand-name" x="475" y="210" font-size="52" fill="var(--paper)" textLength="345" lengthAdjust="spacingAndGlyphs">Tollworth Marks</text>
      <text class="tagline" x="476" y="229" font-size="17" fill="var(--paper)" textLength="273" lengthAdjust="spacingAndGlyphs">SHARP PRINTS, FAST TURNAROUND</text>
    </g>

    <polygon class="fill-ink" points="1333,1253 1333,1392 1227,1392"/>
    <polygon class="fill-red" points="812,1395 1333,1392 1333,1440 779,1440"/>
    <polygon class="fill-red" points="360,1438 700,1440 612,1552 275,1552"/>
    <polygon class="fill-ink" points="723,1440 1333,1440 1333,1478 1227,1627 257,1627 257,1568 620,1568"/>
    <polygon class="fill-steel" points="1333,1478 1333,1627 1227,1627"/>
    <g class="letterhead-social">
      <circle class="fill-ink" cx="423" cy="1475" r="12"/>
      <text class="contact" x="441" y="1480" font-size="16">@tollworthmarks</text>
      <circle class="fill-ink" cx="421" cy="1514" r="12"/>
      <text class="contact" x="438" y="1518" font-size="16">@tollworthmarks</text>
    </g>
    <g class="letterhead-contact">
      <circle class="fill-red" cx="743" cy="1513" r="12"/>
      <text class="contact" x="760" y="1516" font-size="15">Lorem ipsum dolor mirid proud</text>
      <circle class="fill-red" cx="741" cy="1553" r="12"/>
      <text class="contact" x="758" y="1556" font-size="15">00 000 0000</text>
      <circle class="fill-red" cx="1039" cy="1514" r="12"/>
      <text class="contact" x="1056" y="1517" font-size="15">info@tollworthmarks.com</text>
      <circle class="fill-red" cx="1041" cy="1553" r="12"/>
      <text class="contact" x="1058" y="1556" font-size="15">www.tollworthmarks</text>
    </g>
  </g>

  <!-- Envelope -->
  <g class="envelope">
    <g class="sheet">
      <path class="fill-red" d="M873,638 V553 Q873,443 983,443 H1934 Q2044,443 2044,553 V638 Z"/>
      <rect class="fill-paper" x="873" y="638" width="1171" height="521"/>
    </g>
    <g class="flap-logo" transform="rotate(180 1455 545)">
      <rect class="fill-paper" x="1150" y="496" width="80" height="94"/>
      <text class="brand-name" x="1253" y="560" font-size="66" fill="var(--paper)" textLength="509" lengthAdjust="spacingAndGlyphs">Tollworth Marks</text>
      <text class="tagline" x="1254" y="588" font-size="23" fill="var(--paper)" textLength="401" lengthAdjust="spacingAndGlyphs">SHARP PRINTS, FAST TURNAROUND</text>
    </g>
    <polygon class="fill-ink" points="873,638 2044,638 2044,680 1365,680 1295,768 873,768"/>
    <polygon class="fill-steel" points="873,638 946,638 873,740"/>
    <polygon class="fill-red" points="1370,690 2044,690 2044,718 1348,718"/>
    <polygon class="fill-red" points="873,768 1255,768 1233,799 873,799"/>
    <polygon class="fill-ink" points="873,799 946,799 873,897"/>
    <g class="envelope-logo">
      <rect class="fill-paper" x="975" y="682" width="36" height="43"/>
      <text class="brand-name" x="1022" y="710" font-size="34" fill="var(--paper)" textLength="240" lengthAdjust="spacingAndGlyphs">Tollworth Marks</text>
      <text class="tagline" x="1023" y="724" font-size="12" fill="var(--paper)" textLength="189" lengthAdjust="spacingAndGlyphs">SHARP PRINTS, FAST TURNAROUND</text>
    </g>
    <polygon class="fill-ink" points="2044,900 2044,997 1972,997"/>
    <polygon class="fill-red" points="1685,999 2044,997 2044,1028 1662,1028"/>
    <polygon class="fill-red" points="1371,1028 1606,1028 1547,1107 1312,1107"/>
    <polygon class="fill-ink" points="1622,1030 2044,1030 2044,1055 1970,1159 873,1159 873,1119 1552,1119"/>
    <polygon class="fill-steel" points="2044,1055 2044,1159 1970,1159"/>
    <g class="envelope-social">
      <circle class="fill-ink" cx="1415" cy="1054" r="8"/>
      <text class="contact" x="1427" y="1057" font-size="10">@tollworthmarks</text>
      <circle class="fill-ink" cx="1413" cy="1081" r="8"/>
      <text class="contact" x="1425" y="1084" font-size="10">@tollworthmarks</text>
    </g>
    <g class="envelope-contact">
      <circle class="fill-red" cx="1636" cy="1080" r="8"/>
      <text class="contact" x="1648" y="1083" font-size="10">Lorem ipsum dolor mirid proud</text>
      <circle class="fill-red" cx="1635" cy="1107" r="8"/>
      <text class="contact" x="1647" y="1110" font-size="10">00 000 0000</text>
      <circle class="fill-red" cx="1840" cy="1080" r="8"/>
      <text class="contact" x="1852" y="1083" font-size="10">info@tollworthmarks.com</text>
      <circle class="fill-red" cx="1842" cy="1107" r="8"/>
      <text class="contact" x="1854" y="1110" font-size="10">www.tollworthmarks</text>
    </g>
  </g>

  <!-- Business card front -->
  <g class="card-front">
    <rect class="sheet fill-paper" x="124" y="622" width="456" height="260"/>
    <rect class="fill-red" x="193" y="830" width="317" height="9"/>
    <rect class="fill-ink" x="124" y="840" width="456" height="42"/>
    <rect class="fill-red" x="148" y="695" width="52" height="62"/>
    <text class="brand-name" x="215" y="738" font-size="44" fill="var(--ink)" textLength="340" lengthAdjust="spacingAndGlyphs">Tollworth Marks</text>
    <text class="tagline" x="217" y="756" font-size="16" fill="var(--muted)" textLength="267" lengthAdjust="spacingAndGlyphs">SHARP PRINTS, FAST TURNAROUND</text>
  </g>

  <!-- Business card back -->
  <g class="card-back">
    <rect class="sheet fill-paper" x="124" y="909" width="456" height="260"/>
    <rect class="fill-red" x="338" y="953" width="8" height="180"/>
    <rect class="fill-ink" x="346" y="909" width="234" height="260"/>
    <text class="person" x="142" y="1045" font-size="30" letter-spacing="-1" textLength="174" lengthAdjust="spacingAndGlyphs"><tspan fill="var(--brand-red)">MARA</tspan> <tspan fill="var(--ink)">KELLET</tspan></text>
    <text class="person" x="142" y="1059" font-size="13" fill="var(--brand-red)" text-decoration="underline" textLength="96" lengthAdjust="spacingAndGlyphs">PROFESSONAL</text>
    <text class="person" x="250" y="1059" font-size="13" fill="var(--muted)" textLength="65" lengthAdjust="spacingAndGlyphs">DIRECTOR</text>
    <g class="card-contact">
      <circle class="fill-red" cx="380" cy="952" r="12"/>
      <text class="contact" x="397" y="956" font-size="12" textLength="162" lengthAdjust="spacingAndGlyphs">Lorem ipsum dolor mirid proud</text>
      <circle class="fill-red" cx="380" cy="988" r="12"/>
      <text class="contact" x="397" y="992" font-size="12">00 000 0000</text>
      <circle class="fill-red" cx="380" cy="1024" r="12"/>
      <text class="contact" x="397" y="1028" font-size="12" textLength="143" lengthAdjust="spacingAndGlyphs">info@tollworthmarks.com</text>
      <circle class="fill-red" cx="380" cy="1060" r="12"/>
      <text class="contact" x="397" y="1064" font-size="12">www.tollworthmarks</text>
      <circle class="fill-red" cx="380" cy="1096" r="12"/>
      <text class="contact" x="397" y="1100" font-size="12">@tollworthmarks</text>
      <circle class="fill-red" cx="380" cy="1132" r="12"/>
      <text class="contact" x="397" y="1136" font-size="12">@tollworthmarks</text>
    </g>
  </g>
</svg>
</body>
</html>
```